New Banner Ad Design Project

We are a start-up in San Francisco that sells consignment clothes with a percentage of the proceeds donated to charity. Also, volunteer groups can conduct dress drives and send them to us and we will sell them and give their charity back 60% of the proceeds.

We have several uses for banners:
- Home page banner:
- Promote timely Flash Sales (they last only 96 hours) which happen 2x/week
- Promote how good it feels to give back and shop
- Promote any special promotions such as a Gift With Purchase
- Community banner:
- Promote the lifestyle
- Promote any particular group conducting a dress drive

If you are going to submit one banner it is to be for an upcoming sale, as the two attached files address (maternity sale). If we find the right designer we will consider working with them beyond the design contest for future sale banners as well as others

We consider our 'competitors' to be The Garment Harbor, The TrueLoop, WovaSpin, KnitPeak, GlowAgain. Our key differentiator is the charitable components and how groups are conducting dress drives to raise money.

We are in the midst of changing our company name, tagline and logo. The new company will be called 'TessaLume' and our tagline is 'Restitched Kindness'

Target Market(s)

Our initial audience is young women 16 - 30. We will be focusing on Prom February through May which appeals to 16 - 18 year olds.

We also have maternity-wear. We want these women to feel fashionable

We are focused on individuals who want to give back.

Industry/Entity Type

Charity

Font styles to use
Serif
Sans Serif

Colors
8769ae
1b1b1b
474747
c3c3c3
86cfc6
b7a5cd

Requirements
Must have
• - Youthful and stylish voice (not to be confused with Young)
- Appealing visuals
- Powerful call-to-action as it pertains to banners for our flash sales
- An inclusive feel
- Communicates our charitable component
Nice to have
• - Emotional appeal
- Women wearing our clothes (see attached)
Should not have
• - Too much text
- Too girly; overly flowery

```html
<!DOCTYPE html>
<html lang="en">
<head>
<meta charset="utf-8">
<title>Maternity Sale Banner</title>
<link rel="stylesheet" href="https://fonts.googleapis.com/css2?family=Playfair+Display:wght@800&family=Josefin+Sans:wght@400&display=swap">
<style>
  :root {
    --violet: #8769ae;
    --violet-bright: #8a72f0;
    --violet-soft: #9783f2;
    --lilac: #b7a5cd;
    --ink: #1b1b1b;
    --charcoal: #474747;
    --silver: #c3c3c3;
    --mint: #86cfc6;
    --paper: #ffffff;
  }
  * { margin: 0; padding: 0; box-sizing: border-box; }
  html, body {
    width: 1200px;
    height: 857px;
    overflow: hidden;
    background: var(--paper);
  }
  .canvas {
    position: relative;
    width: 1200px;
    height: 857px;
  }
  .banner {
    position: absolute;
    left: 29px;
    top: 238px;
    width: 1142px;
    height: 380px;
    overflow: hidden;
    background: radial-gradient(ellipse at 62% 55%, var(--violet-soft) 0%, var(--violet-bright) 75%);
  }
  .ornament {
    position: absolute;
  }
  .ornament--left {
    left: 0;
    top: 120px;
    width: 200px;
    height: 260px;
    background: radial-gradient(ellipse at 30% 75%, rgba(71,71,71,0.55), rgba(134,207,198,0.35) 45%, rgba(134,207,198,0) 72%);
  }
  .ornament--right {
    right: 0;
    top: 0;
    width: 290px;
    height: 380px;
    background:
      radial-gradient(ellipse at 80% 80%, rgba(71,71,71,0.5), rgba(134,207,198,0.35) 40%, rgba(195,195,195,0) 70%),
      radial-gradient(ellipse at 90% 15%, rgba(134,207,198,0.45), rgba(134,207,198,0) 45%);
  }
  .photo-frame {
    position: absolute;
    left: 90px;
    top: 0;
    width: 298px;
    height: 380px;
    background: #2f2f2f;
  }
  .photo {
    position: absolute;
    left: 22px;
    top: 0;
    width: 254px;
    height: 380px;
    background: linear-gradient(180deg, #b9b3a8 0%, #8f8a78 40%, #cbbd9f 70%, #d6c7a8 100%);
  }
  .headline {
    position: absolute;
    left: 400px;
    top: 38px;
    width: 656px;
    text-align: center;
    font-family: "Playfair Display", Georgia, serif;
    font-weight: 800;
    font-size: 124px;
    line-height: 103px;
    color: var(--ink);
    letter-spacing: -1px;
    transform: scaleX(0.85);
  }
  .brand-card {
    position: absolute;
    left: 553px;
    top: 280px;
    width: 338px;
    height: 91px;
    background: var(--paper);
    display: flex;
    flex-direction: column;
    align-items: center;
    justify-content: center;
    font-family: "Josefin Sans", Arial, sans-serif;
  }
  .brand-name {
    font-size: 36px;
    letter-spacing: 4px;
    color: var(--ink);
    line-height: 1;
  }
  .brand-tagline {
    margin-top: 6px;
    font-size: 13px;
    letter-spacing: 5.5px;
    color: var(--violet);
  }
</style>
</head>
<body>
  <div class="canvas">
    <section class="banner">
      <div class="ornament ornament--left" role="img" aria-label="Dark and mint flourish ornament"></div>
      <div class="ornament ornament--right" role="img" aria-label="Dark, mint and grey flourish ornament"></div>
      <div class="photo-frame">
        <div class="photo" role="img" aria-label="Photo: expectant mother in a patterned maternity dress with a dark sash, standing on a tree-lined city walkway"></div>
      </div>
      <h1 class="headline">MATERNITY<br>SALE</h1>
      <div class="brand-card">
        <span class="brand-name">TESSALUME</span>
        <span class="brand-tagline">RESTITCHED KINDNESS</span>
      </div>
    </section>
  </div>
</body>
</html>
```